Brelvora company website, a website for employment for people with autism

The website will make a match between people and jobs, mainly in the graphical sector, but also other sectors.
The name of the company is brelvora and automates jobs with people that are on the autism spectrum.
The whole matchmaking and feedback process and so doesn't have to be in this prototype, we just want the general information pages and to convey a great look and brand identity that we will keep in the other pages to be developed. The website must be made with Wordpress, since the backend will be developed in Wordpress too.
It is a social project that wants to create possibilites for people with ASS to work from home for an employer or to do a variety of tasks for different customers.
The people we hire are generally not on the regular job market or have difficulty finding a job and "selling themselves"

Target Market(s)

matchmaking between talent (with ASS) and employers / jobs

Number of Pages Required

5+ page

Font styles to use
Sans Serif

Colors
ec1f27
e34298
a64599
6b449b
0355a3
0792cd

Requirements
Must have
• A stunning landing pages
• Integrate our logo and must match with what will do. We want a clean, modern, minimalistic, sleek website that radiates creativity and good looks.
• We have one page describing what we can do for customers, one page for people with ASS that would like to be candidates (our approach, learning program, ...), two pages that are addressed to partners who want to cooperate: the one's that can assist with autism related assistance and the one's that can help with the job coaching.
Nice to have
• In our logo are many colors as we embrace diversity and want to show that. Out main branding colors are red (for action) and blue for stability and will all gradients that go with it. Mainly white or black (or anthracite) for other parts
Should not have
• We want a modern and minimalistic design, no fluffy designs with lots of ornaments.

```html
<!DOCTYPE html>
<html lang="en">
<head>
<meta charset="utf-8">
<title>Brelvora</title>
<link href="https://fonts.googleapis.com/css2?family=Montserrat:wght@500;600;700;800&family=Open+Sans:wght@400;600&display=swap" rel="stylesheet">
<style>
:root{
  --red:#ec1f27;
  --pink:#e34298;
  --violet:#a64599;
  --purple:#6b449b;
  --blue:#0355a3;
  --sky:#0792cd;
  --navy:#0a3f94;
  --ink:#1b1b1b;
  --anthracite:#2b2b2b;
  --text:#3a3a3a;
  --line:#d9d9d9;
  --white:#ffffff;
}
*{box-sizing:border-box;margin:0;padding:0}
html,body{width:1200px;height:3422px;overflow:hidden}
body{position:relative;background:var(--white);font-family:"Open Sans",Arial,sans-serif;color:var(--text)}
.abs{position:absolute}
.heading{font-family:"Montserrat",Arial,sans-serif;font-weight:600;color:var(--ink);letter-spacing:1px}

/* hero */
.hero-photo{left:0;top:0;width:1200px;height:860px}
.brand{left:114px;top:95px;font-family:"Montserrat",Arial,sans-serif;font-weight:600;font-size:30px;letter-spacing:5px;color:var(--white);display:flex;align-items:center;gap:12px}
.brand-dot{width:14px;height:14px;border-radius:50%;background:var(--white)}
.menu{left:1052px;top:64px;width:34px;height:28px;display:flex;flex-direction:column;justify-content:space-between}
.menu span{display:block;height:5px;background:var(--white);border-radius:2px}
.hero-title{left:0;width:1200px;top:305px;text-align:center;font-family:"Montserrat",Arial,sans-serif;font-weight:800;font-size:104px;color:var(--white);letter-spacing:3px}
.hero-text{left:300px;width:600px;top:437px;text-align:center;font-size:16px;line-height:34px;color:var(--white)}
.btn-solid{display:flex;align-items:center;justify-content:center;gap:10px;background:var(--red);color:var(--white);font-family:"Montserrat",Arial,sans-serif;font-weight:600;font-size:17px;clip-path:polygon(8% 0,92% 0,100% 50%,92% 100%,8% 100%,0 50%)}
.btn-arrow{width:17px;height:17px;border-radius:50%;background:currentColor;position:relative}
.btn-solid .btn-arrow{background:var(--white)}
.btn-arrow::after{content:"";position:absolute;left:5px;top:4px;border-left:7px solid var(--red);border-top:4.5px solid transparent;border-bottom:4.5px solid transparent}
.hero-btn{left:480px;top:545px;width:240px;height:60px}
.scroll{left:584px;top:708px}

/* decorative areas */
.deco{opacity:.35}

/* about */
.about-title{left:114px;top:1090px;font-size:44px}
.about-text{left:114px;top:1175px;width:380px;font-size:13px;line-height:32px;color:#555}
.btn-outline{left:114px;top:1432px;width:172px;height:46px}
.btn-outline-label{left:114px;top:1432px;width:172px;height:46px;display:flex;align-items:center;justify-content:center;gap:8px;font-family:"Montserrat",Arial,sans-serif;font-weight:600;font-size:14px;color:var(--red)}
.btn-outline-label .btn-arrow{background:var(--red)}
.btn-outline-label .btn-arrow::after{border-left-color:var(--white)}

/* services */
.services-title{left:707px;top:1935px;font-size:44px;color:var(--white)}
.services-text{left:708px;top:2012px;width:380px;font-size:13px;line-height:26px;color:var(--white)}
.service{left:708px;display:flex;align-items:center;gap:18px;color:var(--white);font-family:"Montserrat",Arial,sans-serif;font-weight:600;font-size:16px;line-height:24px}
.service svg{flex:none}

/* contact */
.contact-title{left:0;width:1200px;top:2692px;text-align:center;font-size:44px}
.info{display:flex;align-items:center;gap:16px;font-size:13px;line-height:22px;color:#444}
.field{border:1px solid var(--line);background:var(--white);font-size:13px;color:#555;padding:0 24px;display:flex;align-items:center}
.field-message{align-items:flex-start;padding-top:16px}
.submit{left:484px;top:3152px;width:232px;height:48px;font-size:15px}

/* footer */
.footer{left:0;top:3335px;width:1200px;height:87px;background:var(--anthracite)}
.copyright{left:114px;top:3366px;font-size:12px;color:var(--white)}
.social{top:3355px;width:46px;height:48px}
</style>
</head>
<body>

<!-- HERO -->
<svg class="abs hero-photo" viewBox="0 0 1200 860" role="img" aria-label="Black and white photograph of a smiling young man in a suit and tie sitting at a laptop">
  <defs>
    <linearGradient id="heroGrad" x1="0" y1="0" x2="1" y2="1">
      <stop offset="0" stop-color="#6e6e6e"/>
      <stop offset=".5" stop-color="#2e2e2e"/>
      <stop offset="1" stop-color="#111"/>
    </linearGradient>
  </defs>
  <polygon points="0,0 1200,0 1200,640 775,856 308,752 0,45" fill="url(#heroGrad)"/>
</svg>

<div class="abs brand"><span class="brand-dot"></span>BRELVORA</div>
<div class="abs menu"><span></span><span></span><span></span></div>
<h1 class="abs hero-title">BRELVORA</h1>
<p class="abs hero-text">Sed ut perspiciatis unde omnis iste natus error sit voluptatem accusantium veritatis et quasi architecto beatae vitae dicta sunt explicabo.</p>
<a class="abs btn-solid hero-btn">READ MORE <span class="btn-arrow"></span></a>
<svg class="abs scroll" width="32" height="68" viewBox="0 0 32 68">
  <rect x="3" y="2" width="26" height="40" rx="13" fill="none" stroke="#fff" stroke-width="2.5"/>
  <line x1="16" y1="10" x2="16" y2="18" stroke="#fff" stroke-width="2.5" stroke-linecap="round"/>
  <polyline points="9,48 16,55 23,48" fill="none" stroke="#fff" stroke-width="2.5"/>
  <polyline points="9,57 16,64 23,57" fill="none" stroke="#fff" stroke-width="2.5"/>
</svg>

<!-- left decorative area -->
<svg class="abs deco" style="left:0;top:680px" width="190" height="340" viewBox="0 0 190 340" role="img" aria-label="Decorative multicolour ornament">
  <defs><linearGradient id="decoLeft" x1="0" y1="0" x2="1" y2="1"><stop offset="0" stop-color="var(--pink)"/><stop offset="1" stop-color="var(--sky)"/></linearGradient></defs>
  <polygon points="0,0 160,30 185,200 60,340 0,320" fill="url(#decoLeft)" opacity=".35"/>
</svg>

<!-- ABOUT -->
<h2 class="abs heading about-title">ABOUT US</h2>
<div class="abs about-text">
  <p>Sed ut perspiciatis unde omnis iste natus error sit voluptatem accusantium doloremque laudantium, totam rem aperiam, eaque ipsa quae ab illo inventore veritatis et quasi architecto beatae vitae dicta sunt explicabo.</p>
  <p>Nemo enim ipsam voluptatem quia voluptas sit aspernatur aut odit aut fugit, sed quia consequuntur</p>
</div>
<svg class="abs btn-outline" viewBox="0 0 172 46"><polygon points="14,1 158,1 171,23 158,45 14,45 1,23" fill="none" stroke="var(--red)" stroke-width="2"/></svg>
<div class="abs btn-outline-label">READ MORE <span class="btn-arrow"></span></div>

<svg class="abs" style="left:930px;top:845px" width="270" height="690" viewBox="0 0 270 690">
  <polygon points="270,0 270,690 240,690 0,540 0,180" fill="none" stroke="var(--red)" stroke-width="5" transform="translate(10,-10)"/>
</svg>
<svg class="abs" style="left:940px;top:855px" width="260" height="680" viewBox="0 0 260 680" role="img" aria-label="Red-tinted photograph of a young man smiling">
  <defs><linearGradient id="redGrad" x1="0" y1="0" x2="1" y2="1"><stop offset="0" stop-color="#f04a55"/><stop offset="1" stop-color="#d8101c"/></linearGradient></defs>
  <polygon points="260,0 260,680 0,530 0,170" fill="url(#redGrad)"/>
</svg>

<!-- centre decorative area -->
<svg class="abs deco" style="left:250px;top:1395px" width="480" height="500" viewBox="0 0 480 500" role="img" aria-label="Decorative pastel ornament">
  <defs><linearGradient id="decoCentre" x1="0" y1="0" x2="1" y2="1"><stop offset="0" stop-color="#f3b8da"/><stop offset=".6" stop-color="#c7c0e3"/><stop offset="1" stop-color="#b6d2ee"/></linearGradient></defs>
  <polygon points="240,5 475,125 475,375 240,495 5,375 5,125" fill="url(#decoCentre)" opacity=".3" transform="rotate(8 240 250)"/>
</svg>

<svg class="abs" style="left:560px;top:920px" width="450" height="500" viewBox="0 0 450 500" role="img" aria-label="Photograph of a smiling young man writing at a desk">
  <defs><linearGradient id="aboutGrad" x1="0" y1="0" x2="1" y2="1"><stop offset="0" stop-color="#4f6b3a"/><stop offset=".55" stop-color="#b8b2aa"/><stop offset="1" stop-color="#6e6a66"/></linearGradient></defs>
  <polygon points="225,0 450,125 450,375 225,500 0,375 0,125" fill="url(#aboutGrad)"/>
</svg>
<svg class="abs" style="left:773px;top:1365px" width="318" height="362" viewBox="0 0 318 362" role="img" aria-label="Photograph of hands typing on a laptop at a desk">
  <defs><linearGradient id="laptopGrad" x1="0" y1="0" x2="1" y2="1"><stop offset="0" stop-color="#e8e4df"/><stop offset=".6" stop-color="#9a8f86"/><stop offset="1" stop-color="#5d5650"/></linearGradient></defs>
  <polygon points="159,0 318,90 318,272 159,362 0,272 0,90" fill="url(#laptopGrad)"/>
</svg>

<!-- SERVICES -->
<svg class="abs" style="left:0;top:1740px" width="1200" height="920" viewBox="0 0 1200 920">
  <polygon points="612,148 1200,30 1200,868 800,908" fill="none" stroke="var(--sky)" stroke-width="4"/>
  <polyline points="0,80 150,40 378,170" fill="none" stroke="var(--navy)" stroke-width="5"/>
</svg>
<svg class="abs" style="left:0;top:1820px" width="700" height="730" viewBox="0 0 700 730" role="img" aria-label="Blue-tinted photograph of a young man in a suit working at a desk">
  <defs><linearGradient id="servPhoto" x1="0" y1="0" x2="1" y2="1"><stop offset="0" stop-color="#2f6fb8"/><stop offset=".6" stop-color="#1c5aa6"/><stop offset="1" stop-color="#3f86c8"/></linearGradient></defs>
  <polygon points="0,80 150,0 600,250 690,510 500,730 0,700" fill="url(#servPhoto)"/>
</svg>
<svg class="abs" style="left:0;top:1750px" width="1200" height="880" viewBox="0 0 1200 880">
  <defs><linearGradient id="servPanel" x1="0" y1="0" x2="1" y2="1"><stop offset="0" stop-color="#0d4aa3"/><stop offset="1" stop-color="var(--navy)"/></linearGradient></defs>
  <polygon points="628,120 1200,6 1200,845 830,873" fill="url(#servPanel)"/>
</svg>
<h2 class="abs heading services-title">SERVICES</h2>
<p class="abs services-text">Sed ut perspiciatis unde omnis iste natus error sit voluptatem accusantium doloremque laudantium, totam rem aperiam, beatae vitae dicta sunt explicabo.</p>
<svg class="abs" style="left:737px;top:2190px" width="2" height="180"><line x1="1" y1="0" x2="1" y2="180" stroke="#fff" stroke-width="1.5" stroke-dasharray="2 4"/></svg>

<div class="abs service" style="top:2120px">
  <svg width="60" height="66" viewBox="0 0 60 66"><polygon points="30,2 57,17 57,49 30,64 3,49 3,17" fill="var(--navy)" stroke="#fff" stroke-width="2"/><circle cx="30" cy="22" r="3" fill="#fff"/><path d="M28 27v10h9l4 8M26 31a8 8 0 1 0 9 12" fill="none" stroke="#fff" stroke-width="2.4" stroke-linecap="round"/></svg>
  <span>Nemo enim ipsam<br>voluptate</span>
</div>
<div class="abs service" style="top:2245px">
  <svg width="60" height="66" viewBox="0 0 60 66"><polygon points="30,2 57,17 57,49 30,64 3,49 3,17" fill="var(--navy)" stroke="#fff" stroke-width="2"/><path d="M20 31h5v12h-5zM27 31l5-9c2 0 3 1 3 3l-1 5h7c2 0 3 2 2 3l-2 8c-1 2-2 2-3 2H27z" fill="#fff"/></svg>
  <span>Reprehenderit qui in ea<br>voluptate velit</span>
</div>
<div class="abs service" style="top:2370px">
  <svg width="60" height="66" viewBox="0 0 60 66"><polygon points="30,2 57,17 57,49 30,64 3,49 3,17" fill="var(--navy)" stroke="#fff" stroke-width="2"/><circle cx="27" cy="22" r="3" fill="#fff"/><path d="M25 27v10h8l3 7M23 31a7 7 0 1 0 8 11M35 36h7v6" fill="none" stroke="#fff" stroke-width="2.2" stroke-linecap="round"/></svg>
  <span>Excepteur sint occaecat<br>cupidatat</span>
</div>

<!-- CONTACT -->
<h2 class="abs heading contact-title">CONTACT US</h2>

<div class="abs info" style="left:246px;top:2812px">
  <svg width="50" height="54" viewBox="0 0 50 54"><polygon points="25,2 47,14 47,40 25,52 3,40 3,14" fill="none" stroke="#f2c61f" stroke-width="2"/><path d="M25 16a7 7 0 0 0-7 7c0 5 7 13 7 13s7-8 7-13a7 7 0 0 0-7-7z" fill="none" stroke="#f2c61f" stroke-width="2.2"/><circle cx="25" cy="23" r="2.4" fill="#f2c61f"/></svg>
  <span>23,Sed ut perspiciatis unde<br>omnis iste natus</span>
</div>
<div class="abs info" style="left:520px;top:2812px">
  <svg width="50" height="54" viewBox="0 0 50 54"><polygon points="25,2 47,14 47,40 25,52 3,40 3,14" fill="none" stroke="var(--violet)" stroke-width="2"/><path d="M17 18c0 10 8 18 18 18l2-5-5-3-3 3c-3-1-6-4-7-7l3-3-3-5z" fill="var(--violet)"/></svg>
  <span>Call Us:<br>1 888 888 888</span>
</div>
<div class="abs info" style="left:726px;top:2812px">
  <svg width="50" height="54" viewBox="0 0 50 54"><polygon points="25,2 47,14 47,40 25,52 3,40 3,14" fill="var(--sky)"/><rect x="14" y="19" width="22" height="16" rx="1" fill="#fff"/><polyline points="14,20 25,29 36,20" fill="none" stroke="var(--sky)" stroke-width="2"/></svg>
  <span>Email us :<br>info@companyname.com</span>
</div>

<div class="abs field" style="left:230px;top:2914px;width:358px;height:42px">Enter Name</div>
<div class="abs field" style="left:611px;top:2914px;width:359px;height:42px">Enter Email</div>
<div class="abs field" style="left:230px;top:2978px;width:358px;height:42px">Phone</div>
<div class="abs field" style="left:611px;top:2978px;width:359px;height:42px">Address</div>
<div class="abs field field-message" style="left:230px;top:3042px;width:740px;height:78px">Message</div>
<a class="abs btn-solid submit">SUBMIT MESSAGE <span class="btn-arrow"></span></a>

<!-- bottom-left decorative area -->
<svg class="abs deco" style="left:0;top:3115px" width="120" height="210" viewBox="0 0 120 210" role="img" aria-label="Decorative multicolour ornament">
  <defs><linearGradient id="decoBottom" x1="0" y1="0" x2="1" y2="1"><stop offset="0" stop-color="var(--pink)"/><stop offset="1" stop-color="var(--blue)"/></linearGradient></defs>
  <polygon points="0,15 100,30 115,130 40,210 0,200" fill="url(#decoBottom)" opacity=".35"/>
</svg>

<!-- FOOTER -->
<footer class="abs footer"></footer>
<p class="abs copyright">© 2019 Companyname.All rights reserved.| &nbsp;Privacy policy</p>
<svg class="abs social" style="left:880px" viewBox="0 0 46 48" role="img" aria-label="Social link"><polygon points="23,2 44,13 44,35 23,46 2,35 2,13" fill="none" stroke="#fff" stroke-width="1.6"/></svg>
<svg class="abs social" style="left:934px" viewBox="0 0 46 48" role="img" aria-label="Social link"><polygon points="23,2 44,13 44,35 23,46 2,35 2,13" fill="none" stroke="#fff" stroke-width="1.6"/></svg>
<svg class="abs social" style="left:988px" viewBox="0 0 46 48" role="img" aria-label="Social link"><polygon points="23,2 44,13 44,35 23,46 2,35 2,13" fill="none" stroke="#fff" stroke-width="1.6"/></svg>
<svg class="abs social" style="left:1042px" viewBox="0 0 46 48" role="img" aria-label="Social link"><polygon points="23,2 44,13 44,35 23,46 2,35 2,13" fill="none" stroke="#fff" stroke-width="1.6"/></svg>

</body>
</html>
```